A3 Event Poster for School Fundraiser

We are looking for a bold, engaging, and professional A3 poster design to promote a special school fundraising event. A top athlete will be visiting a primary school to inspire children, encourage participation in sport, and help launch a fundraising initiative to raise money for new PE/sports equipment for the school.

The poster will be displayed prominently outside the school and shared with parents and families. Its purpose is to generate excitement, explain the event quickly, and encourage parents/families to sponsor and get involved.

We work with about 50 different athletes so will need the design to be easy to alter the picture of the athlete/name etc so it can be replicated across the different athletes.

Target Market(s)

Priamary School Parents/Communities

Industry/Entity Type

Education

Font styles to use
Other font styles liked:
• The logo font is Rajdhani. ‘Corvel’ is bold, ‘Pennix’ is semibold and the strapline is regular.

Requirements
Must have
• Space for the Event Date (that school can write in themselves), A picture of the visiting athlete and their bio (with ability to easily change)
Nice to have
• Bold, eye-catching

```html
<!DOCTYPE html>
<html lang="en">
<head>
<meta charset="utf-8">
<title>Inspirational Athlete Visiting Our School</title>
<link rel="stylesheet" href="https://fonts.googleapis.com/css2?family=Poppins:wght@300;400;500;600;700;800&family=Rajdhani:wght@400;600&family=Open+Sans:ital,wght@1,700&display=swap">
<style>
  :root {
    --purple: #7b3596;
    --navy: #17286b;
    --royal: #253a9c;
    --red: #e31b36;
    --cyan: #14a9d1;
    --white: #ffffff;
    --paper: #ffffff;
  }
  * { margin: 0; padding: 0; box-sizing: border-box; }
  html, body { width: 849px; height: 1200px; overflow: hidden; background: var(--paper); }
  .poster {
    position: relative;
    width: 849px;
    height: 1200px;
    overflow: hidden;
    font-family: "Poppins", sans-serif;
    color: var(--white);
  }
  .poster-shapes { position: absolute; inset: 0; }

  .brand {
    position: absolute;
    left: 52px;
    top: 40px;
    display: flex;
    align-items: flex-start;
    gap: 8px;
    font-family: "Rajdhani", sans-serif;
    color: var(--purple);
  }
  .brand-mark { width: 30px; height: 30px; margin-top: 12px; background: var(--red); }
  .brand-name { font-weight: 600; font-size: 50px; line-height: 50px; letter-spacing: 0.5px; }
  .brand-name sup { font-size: 16px; vertical-align: top; line-height: 20px; }
  .brand-tagline { font-weight: 400; font-size: 13px; line-height: 14px; margin-top: 1px; }

  .tilted { position: absolute; transform: rotate(-6.6deg); transform-origin: center; }

  .headline {
    left: 10px;
    top: 160px;
    width: 840px;
    text-align: center;
    font-weight: 800;
    font-size: 74px;
    line-height: 70px;
    letter-spacing: 4px;
    text-transform: uppercase;
  }
  .headline .accent { color: var(--cyan); }
  .headline .line-one { margin-left: -20px; }
  .headline .line-two { margin-left: -10px; }
  .headline .line-three { margin-left: -10px; }

  .role-banner {
    left: 20px;
    top: 388px;
    width: 420px;
    text-align: center;
    font-weight: 700;
    font-size: 35px;
    line-height: 42px;
    text-transform: uppercase;
  }

  .bio { left: 50px; top: 560px; width: 380px; }
  .bio-title { font-weight: 700; font-size: 34px; line-height: 38px; }
  .bio-title::after { content: ""; display: block; width: 58px; height: 4px; background: var(--red); margin-top: 2px; }
  .bio-text { font-weight: 500; font-size: 17.5px; line-height: 30px; letter-spacing: 0.6px; margin-top: 8px; width: 310px; }

  .appeal {
    left: 0px;
    top: 858px;
    width: 849px;
    text-align: center;
    font-weight: 800;
    font-size: 50px;
    line-height: 56px;
    letter-spacing: 1.5px;
    text-transform: uppercase;
  }
  .appeal .line-one { margin-left: 80px; }

  .event-date { position: absolute; left: 118px; top: 1064px; width: 250px; text-align: center; }
  .event-date-label { color: var(--cyan); font-weight: 600; font-size: 29px; line-height: 34px; }
  .event-date-value { font-weight: 300; font-size: 31px; line-height: 36px; letter-spacing: 1px; }

  .divider { position: absolute; left: 436px; top: 1035px; width: 2px; height: 96px; background: var(--white); }

  .benefits { position: absolute; left: 496px; top: 1005px; list-style: none; }
  .benefits li { font-weight: 600; font-size: 29px; line-height: 43px; display: flex; align-items: center; }
  .benefits li::before { content: ""; width: 8px; height: 8px; border-radius: 50%; background: var(--red); margin-right: 14px; }

  .footer-line {
    position: absolute;
    left: 0;
    top: 1147px;
    width: 849px;
    height: 53px;
    background: var(--cyan);
    text-align: center;
    font-family: "Open Sans", sans-serif;
    font-style: italic;
    font-weight: 700;
    font-size: 19px;
    line-height: 53px;
    letter-spacing: 0.4px;
  }
</style>
</head>
<body>
<main class="poster">
  <svg class="poster-shapes" width="849" height="1200" viewBox="0 0 849 1200">
    <defs>
      <linearGradient id="lowerPanel" x1="0" y1="0" x2="1" y2="0">
        <stop offset="0" stop-color="#17286b"/>
        <stop offset="1" stop-color="#253a9c"/>
      </linearGradient>
      <linearGradient id="athletePhoto" x1="0" y1="0" x2="1" y2="1">
        <stop offset="0" stop-color="#3d5aa8"/>
        <stop offset="0.5" stop-color="#a9b8d8"/>
        <stop offset="1" stop-color="#2f4fa3"/>
      </linearGradient>
    </defs>
    <rect class="base-navy" x="0" y="0" width="849" height="1200" fill="var(--navy)"/>
    <polygon class="top-white" points="0,0 849,0 849,62 0,160" fill="var(--white)"/>
    <polygon class="headline-band" points="0,160 849,62 849,315 461,360 0,411" fill="var(--purple)"/>
    <polygon class="role-band" points="0,411 461,360 461,465 0,522" fill="var(--red)"/>
    <polygon class="athlete-photo" role="img" aria-label="Photo of the visiting athlete in team kit" points="461,357 849,315 849,752 461,800" fill="url(#athletePhoto)"/>
    <polygon class="divider-stripe" points="0,855 849,757 849,775 0,873" fill="var(--white)"/>
    <polygon class="appeal-band" points="0,894 849,796 849,963 0,1066" fill="var(--purple)"/>
    <polygon class="details-panel" points="0,1066 849,963 849,1147 0,1147" fill="url(#lowerPanel)"/>
  </svg>

  <header class="brand">
    <span class="brand-mark"></span>
    <div>
      <div class="brand-name">CorvelPennix<sup>®</sup></div>
      <div class="brand-tagline">Sport in every school</div>
    </div>
  </header>

  <h1 class="tilted headline">
    <div class="line-one">Inspirational</div>
    <div class="line-two"><span class="accent">Athlete</span> Visiting</div>
    <div class="line-three">Our School</div>
  </h1>

  <h2 class="tilted role-banner">Olympic<br>Volleyball Player</h2>

  <section class="tilted bio">
    <h3 class="bio-title">BIO:</h3>
    <p class="bio-text">Marcus is a dynamic English volleyball player and coach, known for his leadership on and off the court and his passion for inspiring the next generation through sport.</p>
  </section>

  <h2 class="tilted appeal">
    <div class="line-one">Help us raise funds</div>
    <div>for new sports equipment</div>
  </h2>

  <div class="event-date">
    <div class="event-date-label">EVENT DATE</div>
    <div class="event-date-value">22. AUG. 2026</div>
  </div>

  <div class="divider"></div>

  <ul class="benefits">
    <li>Be inspired</li>
    <li>Make a difference</li>
    <li>Get Active</li>
  </ul>

  <footer class="footer-line">Inspiring every child to lead an active, resilient and healthy life</footer>
</main>
</body>
</html>
```